A Skyline Site needs designs

We need a website design for our new venture which is a Skyline website. This website should have the latest design trends.

Menu
Weather, Maps, Videos and Photos

The home page requirements are as follows:
- Search Bar
- Local Weather
- Weather forecast of major cities in the World
Favorite locations
- Space for ADs
- Email signup

Weather Details page
This page will be redirected from the home page when you click on any of the weather forecast section

We are open to all kinds of designs and ideas. Feel free to you colors which suite your design.

```html
<!DOCTYPE html>
<html lang="en">
<head>
<meta charset="utf-8">
<title>Skyline – Hourly Forecast, San Francisco</title>
<link href="https://fonts.googleapis.com/css2?family=Roboto:wght@300;400;500;700&display=swap" rel="stylesheet">
<style>
:root{
  --page-bg:#11162a;
  --white:#ffffff;
  --brand:#0c5aa8;
  --brand-dark:#0a4a92;
  --brand-deep:#0a4d94;
  --ink:#222;
  --muted:#666;
  --tab-bar:#e0e0e0;
  --row-alt:#f2f2f2;
  --ad-bg:#f0f0f0;
  --ad-text:#a8a8a8;
}
*{box-sizing:border-box;margin:0;padding:0}
html,body{width:1200px;height:1167px;overflow:hidden;background:var(--page-bg);font-family:'Roboto',sans-serif;color:var(--ink)}
.page{position:absolute;left:57px;top:0;width:1087px;height:924px;background:var(--white)}
.site-header{position:absolute;left:0;top:0;width:100%;height:75px;background:var(--white);z-index:2}
.brand{position:absolute;left:0;top:0;width:111px;height:105px;background:var(--brand);display:flex;align-items:center;justify-content:center;gap:6px;color:var(--white);font-size:17px;font-weight:500}
.brand .dot{width:10px;height:10px;border-radius:50%;background:var(--white)}
.main-nav{position:absolute;left:148px;top:0;height:75px;display:flex}
.main-nav a{display:flex;align-items:center;padding:0 16px;font-size:14px;color:#333;text-decoration:none;letter-spacing:.2px}
.main-nav a.active{background:#e4e4e4}
.main-nav a+a{margin-left:0}
.unit{position:absolute;top:21px;width:28px;height:28px;border-radius:50%;font-size:13px;display:flex;align-items:center;justify-content:center;font-weight:500;color:#333}
.unit.c{left:808px;background:#e4e4e4}
.unit.f{left:843px}
.signup{position:absolute;left:917px;top:28px;font-size:13px;color:#333}
.login{position:absolute;left:976px;top:20px;width:84px;height:32px;border:1.5px solid var(--brand);border-radius:16px;color:var(--brand);font-size:13px;font-weight:500;display:flex;align-items:center;justify-content:center}
.hero{position:absolute;left:0;top:75px;width:100%;height:168px;background:linear-gradient(100deg,#2a2230 0%,#7a2a18 30%,#c4471e 50%,#5a2a30 75%,#c0402a 100%)}
.hero h1{position:absolute;left:47px;top:68px;font-size:22px;font-weight:400;color:var(--white)}
.search{position:absolute;left:621px;top:62px;display:flex;height:45px}
.search .field{width:298px;background:var(--white);font-size:14px;color:#555;display:flex;align-items:center;padding-left:23px}
.search .btn{width:108px;background:var(--brand);color:var(--white);font-size:14px;font-weight:700;display:flex;align-items:center;justify-content:center}
.tabs{position:absolute;left:0;top:243px;width:100%;height:47px;background:var(--tab-bar)}
.tabs span{position:absolute;top:0;height:47px;display:flex;align-items:center;font-size:15px;color:#333}
.tabs span.active{background:var(--white);left:103px;width:105px;justify-content:center}
.forecast{position:absolute;left:0;top:315px;width:820px}
.forecast .head{height:35px;background:var(--brand);color:var(--white);font-size:13px;font-weight:500;position:relative}
.forecast .row{height:65px;position:relative;font-size:13px}
.forecast .row:nth-child(odd){background:var(--row-alt)}
.cell{position:absolute;top:0;height:100%;display:flex;align-items:center}
.head .cell{top:0}
.icon{left:22px}
.time{left:63px;flex-direction:column;align-items:flex-start;justify-content:center;line-height:15px}
.time small{font-size:12px;color:var(--muted);font-weight:500}
.temp{font-weight:700}
.ad{position:absolute;left:836px;width:232px;background:var(--ad-bg);color:var(--ad-text);font-size:20px;font-weight:300;text-align:center;line-height:29px;display:flex;align-items:center;justify-content:center}
.footer-nav{position:absolute;left:57px;top:934px;width:1087px;height:41px;background:var(--brand-dark);display:flex;align-items:center}
.footer-nav a{position:absolute;color:var(--white);font-size:14px;font-weight:500;text-decoration:none}
.footer{position:absolute;left:57px;top:975px;width:1087px;height:136px;background:var(--brand)}
.footer .mark{position:absolute;left:39px;top:56px;font-size:16px;color:#7ea9d6;display:flex;align-items:center;gap:6px}
.footer .mark .dot{width:9px;height:9px;border-radius:50%;background:#7ea9d6}
.legal{position:absolute;left:158px;top:49px;color:var(--white);font-size:13px;line-height:21px}
.footer .ad-wide{position:absolute;left:384px;top:23px;width:356px;height:89px;background:var(--brand-deep);color:#8fb4dc;font-size:16px;display:flex;align-items:center;justify-content:center}
.social{position:absolute;left:800px;top:56px;display:flex;gap:22px}
.social span{width:22px;height:22px;border-radius:50%;border:2px solid var(--white)}
</style>
</head>
<body>
<div class="page">
  <header class="site-header">
    <div class="brand"><span class="dot"></span>Skyline</div>
    <nav class="main-nav">
      <a class="active">WEATHER</a><a>MAPS</a><a>VIDEOS</a><a>PHOTOS</a>
    </nav>
    <span class="unit c">C°</span><span class="unit f">F°</span>
    <span class="signup">Sign up</span>
    <span class="login">LOG IN</span>
  </header>

  <section class="hero" role="img" aria-label="Photo of a lit suspension bridge at dusk under a red sky">
    <h1>SAN FRANCISCO, CA</h1>
    <div class="search"><div class="field">Search City, index or airport</div><div class="btn">SEARCH</div></div>
  </section>

  <nav class="tabs">
    <span style="left:36px">Today</span>
    <span class="active">Hourly</span>
    <span style="left:233px">5 Day</span>
    <span style="left:328px">10 Day</span>
    <span style="left:430px">Weekend</span>
    <span style="left:544px">Monthly</span>
    <span style="left:655px">Maps</span>
  </nav>

  <svg width="0" height="0" style="position:absolute">
    <defs>
      <symbol id="rain" viewBox="0 0 32 32">
        <path d="M8 20a6 6 0 0 1 1-11.9A8 8 0 0 1 24 9a5.5 5.5 0 0 1 1 11" fill="none" stroke="#333" stroke-width="2.4" stroke-linecap="round"/>
        <g stroke="#333" stroke-width="2.4" stroke-linecap="round">
          <line x1="11" y1="19" x2="11" y2="21"/><line x1="11" y1="25" x2="11" y2="26"/>
          <line x1="16" y1="21" x2="16" y2="23"/><line x1="16" y1="27" x2="16" y2="29"/>
          <line x1="21" y1="19" x2="21" y2="21"/><line x1="21" y1="25" x2="21" y2="26"/>
        </g>
      </symbol>
    </defs>
  </svg>

  <div class="forecast">
    <div class="head">
      <span class="cell" style="left:23px">TIME</span>
      <span class="cell" style="left:170px">DESCRIPTION</span>
      <span class="cell" style="left:323px">TEMP</span>
      <span class="cell" style="left:411px">FEELS</span>
      <span class="cell" style="left:501px">PRECIP</span>
      <span class="cell" style="left:599px">HUMIDITY</span>
      <span class="cell" style="left:725px">WIND</span>
    </div>
    <div class="rows">
      <div class="row"><span class="cell icon"><svg width="32" height="32"><use href="#rain"/></svg></span><span class="cell time">8:45 PM<small>MON</small></span><span class="cell" style="left:170px">Showers</span><span class="cell temp" style="left:327px">16°</span><span class="cell" style="left:413px">15°</span><span class="cell" style="left:502px">35%</span><span class="cell" style="left:602px">89%</span><span class="cell" style="left:726px">N 21 km/h</span></div>
      <div class="row"><span class="cell icon"><svg width="32" height="32"><use href="#rain"/></svg></span><span class="cell time">8:45 PM<small>MON</small></span><span class="cell" style="left:170px">Showers</span><span class="cell temp" style="left:327px">16°</span><span class="cell" style="left:413px">15°</span><span class="cell" style="left:502px">35%</span><span class="cell" style="left:602px">89%</span><span class="cell" style="left:726px">N 21 km/h</span></div>
      <div class="row"><span class="cell icon"><svg width="32" height="32"><use href="#rain"/></svg></span><span class="cell time">8:45 PM<small>MON</small></span><span class="cell" style="left:170px">Showers</span><span class="cell temp" style="left:327px">16°</span><span class="cell" style="left:413px">15°</span><span class="cell" style="left:502px">35%</span><span class="cell" style="left:602px">89%</span><span class="cell" style="left:726px">N 21 km/h</span></div>
      <div class="row"><span class="cell icon"><svg width="32" height="32"><use href="#rain"/></svg></span><span class="cell time">8:45 PM<small>MON</small></span><span class="cell" style="left:170px">Showers</span><span class="cell temp" style="left:327px">16°</span><span class="cell" style="left:413px">15°</span><span class="cell" style="left:502px">35%</span><span class="cell" style="left:602px">89%</span><span class="cell" style="left:726px">N 21 km/h</span></div>
      <div class="row"><span class="cell icon"><svg width="32" height="32"><use href="#rain"/></svg></span><span class="cell time">8:45 PM<small>MON</small></span><span class="cell" style="left:170px">Showers</span><span class="cell temp" style="left:327px">16°</span><span class="cell" style="left:413px">15°</span><span class="cell" style="left:502px">35%</span><span class="cell" style="left:602px">89%</span><span class="cell" style="left:726px">N 21 km/h</span></div>
      <div class="row"><span class="cell icon"><svg width="32" height="32"><use href="#rain"/></svg></span><span class="cell time">8:45 PM<small>MON</small></span><span class="cell" style="left:170px">Showers</span><span class="cell temp" style="left:327px">16°</span><span class="cell" style="left:413px">15°</span><span class="cell" style="left:502px">35%</span><span class="cell" style="left:602px">89%</span><span class="cell" style="left:726px">N 21 km/h</span></div>
      <div class="row"><span class="cell icon"><svg width="32" height="32"><use href="#rain"/></svg></span><span class="cell time">8:45 PM<small>MON</small></span><span class="cell" style="left:170px">Showers</span><span class="cell temp" style="left:327px">16°</span><span class="cell" style="left:413px">15°</span><span class="cell" style="left:502px">35%</span><span class="cell" style="left:602px">89%</span><span class="cell" style="left:726px">N 21 km/h</span></div>
      <div class="row"><span class="cell icon"><svg width="32" height="32"><use href="#rain"/></svg></span><span class="cell time">8:45 PM<small>MON</small></span><span class="cell" style="left:170px">Showers</span><span class="cell temp" style="left:327px">16°</span><span class="cell" style="left:413px">15°</span><span class="cell" style="left:502px">35%</span><span class="cell" style="left:602px">89%</span><span class="cell" style="left:726px">N 21 km/h</span></div>
    </div>
  </div>

  <aside class="ad" style="top:308px;height:264px">YOUR ADS<br>BANNER<br>GOES HERE</aside>
  <aside class="ad" style="top:591px;height:279px">YOUR ADS<br>BANNER<br>GOES HERE</aside>
</div>

<nav class="footer-nav">
  <a style="left:39px">WEATHER</a><a style="left:146px">MAPS</a><a style="left:230px">VIDEOS</a><a style="left:322px">PHOTOS</a>
</nav>
<footer class="footer">
  <div class="mark"><span class="dot"></span>Skyline</div>
  <p class="legal">©2017 Skyline Forecast, Inc.<br>All rights reserved.</p>
  <div class="ad-wide">YOUR ADS BANNER GOES HERE</div>
  <div class="social"><span></span><span></span><span></span><span></span><span></span><span></span></div>
</footer>
</body>
</html>
```